Redesign Current Website Into An Exciting Updated Design

We need to redesign the current website www.glintvaultoffers.net We want an overall new look. We are rebranding so it will be a new logo and we would like to see new images as well so you cannot compare the old from the new.

You can use same exact content as on current url www.glintvaultoffers.net

The website must be warm and inviting and fun yet professional and modern.

The website must also be designed with mobile in mind

The website must be warm and inviting yet professional and modern.

The website must also be designed with mobile in mind.

Target Market(s)

Consumers redeeming rewards

Industry/Entity Type

Promotional Reward Fullfillment

Coding

Coded - Design and coding required

Number of Pages Required

3 page

Requirements
Must have
• This website is a website where consumers come to redeem rewards they received from doing business with a company that offers these rewards. So the website should be very inviting.
Nice to have
• open
Should not have
• open

```html
<!DOCTYPE html>
<html lang="en">
<head>
<meta charset="utf-8">
<title>Kindly Yours Rewards – Online Redemption</title>
<link rel="stylesheet" href="https://fonts.googleapis.com/css2?family=Bebas+Neue&family=Roboto:ital,wght@0,300;0,400;0,500;1,400&display=swap">
<style>
:root{
  --blue:#2a6897;
  --gold:#c9982f;
  --gold-light:#e0b64d;
  --cream:#f3e4c2;
  --pale:#e9f0f8;
  --ink:#2c2c2c;
  --text:#4a4a4a;
  --white:#ffffff;
}
*{box-sizing:border-box;margin:0;padding:0}
html,body{width:1200px;height:2603px;overflow:hidden}
body{position:relative;font-family:'Roboto',sans-serif;color:var(--text);background:var(--white)}
.abs{position:absolute}
.display{font-family:'Bebas Neue',sans-serif;font-weight:400}

/* header */
.site-header{left:0;top:0;width:1200px;height:81px;background:var(--blue);z-index:3}
.brand{left:111px;top:0;width:171px;height:140px;background:var(--blue);z-index:4;padding:22px 12px 10px}
.brand-frame{width:100%;height:100%;border:2px solid var(--white);display:flex;flex-direction:column;align-items:center;justify-content:center;color:var(--white);font-size:30px;line-height:28px;text-align:center}
.main-nav{right:140px;top:30px;display:flex;gap:62px}
.main-nav a{color:var(--white);text-decoration:none;font-size:17px;letter-spacing:.3px}

/* hero */
.hero{left:0;top:81px;width:1200px;height:469px;background:radial-gradient(circle at 22% 30%,#f2e6e2 0,#e6d3cf 40%,#d9c2bc 100%)}
.hero-art{left:588px;top:100px;width:560px;height:380px;border-radius:24px;background:radial-gradient(ellipse at 40% 50%,#f7efe9 0,#e8c7a0 45%,rgba(217,194,188,0) 72%)}
.hero-title{left:111px;top:200px;font-size:42px;line-height:49px;color:var(--blue);letter-spacing:.5px}
.hero-copy{left:111px;top:316px;width:456px;font-size:15px;line-height:23px;color:var(--ink)}
.field{left:111px;width:256px;height:34px;border:1px solid #9a8f8a;border-radius:7px;background:rgba(255,255,255,.35);font-size:13px;color:#333;padding:9px 10px}
.send-btn{left:378px;top:450px;width:46px;height:34px;border-radius:7px;background:var(--blue);display:flex;align-items:center;justify-content:center}

/* categories */
.category{top:622px;width:170px;text-align:center;color:var(--blue);font-size:19px;line-height:22px}
.category svg{display:block;margin:0 auto 24px}
.category.is-active{color:var(--gold)}
.divider{top:640px;width:3px;height:108px;background:var(--gold-light)}
.redeem-btn{left:519px;top:822px;width:162px;height:34px;background:var(--blue);border-radius:7px;color:var(--white);font-size:15px;display:flex;align-items:center;justify-content:center}

/* about */
.about{left:0;top:960px;width:1200px;height:1153px;background:var(--pale)}
.voucher-photo{left:111px;top:1046px;width:246px;height:268px;background:linear-gradient(180deg,var(--gold) 0,#c69a38 100%);padding:24px 13px}
.voucher-photo span{display:block;height:106px;margin-bottom:8px;background:linear-gradient(135deg,#5ec3ec,#e8f6fc)}
.dining-photo{left:372px;top:1049px;width:216px;height:161px;background:linear-gradient(135deg,#3b2a22,#a0703f 55%,#d9b07a)}
.card-photo{left:372px;top:1226px;width:216px;height:268px;background:linear-gradient(160deg,#8a9aa6,#d7c2ae 55%,#6c7b86)}
.about-brand{left:137px;top:1392px;width:180px;color:var(--blue);font-size:42px;line-height:38px;border-left:2px solid var(--blue);border-bottom:2px solid var(--blue);padding:0 0 8px 10px}
.section-title{color:var(--blue);font-size:42px;line-height:42px;border-left:2px solid var(--blue);border-bottom:2px solid var(--blue);padding:18px 12px 6px 8px}
.about-title{left:633px;top:1050px}
.about-copy{left:633px;top:1125px;width:460px;font-size:15px;line-height:23px;color:var(--text)}
.about-copy p{margin-bottom:11px}
.read-more{left:633px;top:1440px;width:100px;height:33px;background:linear-gradient(90deg,var(--gold),var(--gold-light));border-radius:7px;color:var(--white);font-size:15px;display:flex;align-items:center;justify-content:center}

/* testimonials */
.testi-title{left:431px;top:1590px}
.testimonial{top:1705px;width:302px;height:322px;background:var(--white);box-shadow:0 2px 6px rgba(0,0,0,.12);overflow:hidden}
.testimonial blockquote{position:absolute;left:32px;top:46px;width:238px;text-align:center;font-size:15px;line-height:23px;color:var(--text);font-weight:300}
.testimonial svg{position:absolute;left:0;bottom:0}
.testimonial .who{position:absolute;left:0;bottom:16px;width:100%;text-align:center}
.who strong{display:block;font-family:'Bebas Neue',sans-serif;font-weight:400;font-size:21px;color:var(--ink)}
.who em{font-size:12px;color:#444}
.arrow{top:1845px}

/* clients */
.clients-title{left:496px;top:2210px}
.client{top:2303px;width:216px;height:92px;border:1px solid #ddd;border-radius:4px;display:flex;align-items:center;justify-content:center;font-family:'Bebas Neue',sans-serif;font-size:34px;color:var(--blue)}
.dots{left:558px;top:2440px;display:flex;gap:10px}
.dots i{width:13px;height:13px;border-radius:50%;border:1.5px solid var(--blue)}
.dots i.on{background:var(--blue)}

/* footer */
.site-footer{left:0;top:2520px;width:1200px;height:83px;background:var(--blue);color:var(--white);font-size:16px;display:flex;align-items:center;justify-content:center;padding-top:22px}
</style>
</head>
<body>

<header class="abs site-header">
  <nav class="abs main-nav display">
    <a href="#testimonials">Testimonials</a>
    <a href="#redeemed">Already Redeemed?</a>
    <a href="#help">Help</a>
  </nav>
</header>
<div class="abs brand display"><div class="brand-frame">Kindly Yours<br>Rewards</div></div>

<section class="abs hero" role="img" aria-label="Soft blurred bokeh background in blush and beige tones"></section>
<div class="abs hero-art" role="img" aria-label="White gift boxes with gold ribbons beside a red promo code tag"></div>
<h1 class="abs hero-title display">Welcome to the Online<br>Redemption System</h1>
<p class="abs hero-copy">To Learn More About Your Offer Including The Full Details, How It Works, Terms, FAQ's and To Redeem and Activate Your Certificate Please Enter A Valid Certificate Number and Email. Certificate ID</p>
<div class="abs field" style="top:404px">Certificate ID</div>
<div class="abs field" style="top:450px">Enter Email Address</div>
<div class="abs send-btn"><svg width="16" height="16" viewBox="0 0 16 16"><path d="M15 1 1 7l5 2 2 6z" fill="#fff"/></svg></div>

<div class="abs category display" style="left:70px">
  <svg width="90" height="90" viewBox="0 0 90 90" fill="none" stroke="#1d1d1d" stroke-width="2.5"><rect x="3" y="3" width="56" height="84" rx="4"/><rect x="32" y="8" width="54" height="76" rx="4"/><circle cx="59" cy="40" r="17"/><path d="M42 40h34M59 23v34M48 28c7 6 15 6 22 0M48 52c7-6 15-6 22 0"/><rect x="10" y="50" width="18" height="26"/><circle cx="19" cy="60" r="4"/><path d="M10 20h30M10 28h20"/></svg>
  Vacation<br>Certificates
</div>
<div class="abs divider" style="left:261px"></div>
<div class="abs category display is-active" style="left:285px">
  <svg width="90" height="90" viewBox="0 0 90 90" fill="none" stroke="#d4a537" stroke-width="2.5"><path d="M15 5h70v40H15z"/><path d="M5 30l65-8 8 55-65 8z"/><path d="M28 58l30-10M40 44l8 20M30 52l6 4"/></svg>
  Travel<br>Vouchers
</div>
<div class="abs divider" style="left:476px"></div>
<div class="abs category display" style="left:518px">
  <svg width="90" height="90" viewBox="0 0 90 90" fill="none" stroke="#1d1d1d" stroke-width="2.5"><circle cx="45" cy="45" r="16"/><path d="M37 40l8-5 8 5v10l-8 5-8-5zM37 40l8 5 8-5M45 45v10"/><circle cx="45" cy="8" r="6"/><circle cx="45" cy="82" r="6"/><circle cx="8" cy="45" r="6"/><circle cx="82" cy="45" r="6"/><circle cx="15" cy="15" r="6"/><circle cx="75" cy="15" r="6"/><circle cx="15" cy="75" r="6"/><circle cx="75" cy="75" r="6"/><path d="M45 14v15M45 61v15M14 45h15M61 45h15M20 20l13 13M70 20 57 33M20 70l13-13M70 70 57 57"/></svg>
  Digital Electronic<br>Products
</div>
<div class="abs divider" style="left:726px"></div>
<div class="abs category display" style="left:742px">
  <svg width="90" height="90" viewBox="0 0 90 90" fill="none" stroke="#1d1d1d" stroke-width="2.5"><path d="M12 42h66M18 42c0 18 10 28 27 28s27-10 27-28"/><path d="M45 70v12M32 84h26"/><path d="M22 42V22M30 42V12M40 42V20M58 20c8 0 14 8 14 22"/><circle cx="30" cy="10" r="3"/></svg>
  Dining<br>Incentives
</div>
<div class="abs divider" style="left:924px"></div>
<div class="abs category display" style="left:955px">
  <svg width="90" height="90" viewBox="0 0 90 90" fill="none" stroke="#1d1d1d" stroke-width="2.5"><path d="M4 68l70 18 12-46-70-18z"/><path d="M4 60l70 18M4 52l70 18"/><path d="M22 4l6 12 13 2-9 9 2 13-12-6-12 6 2-13-9-9 13-2z"/><rect x="62" y="40" width="16" height="10" rx="2"/></svg>
  Gas &amp; Grocery<br>Rewards
</div>
<div class="abs redeem-btn display">Redeem Your Offer Now</div>

<section class="abs about"></section>
<div class="abs voucher-photo" role="img" aria-label="Two printed travel voucher cards with airplanes on a gold backdrop"><span></span><span></span></div>
<div class="abs dining-photo" role="img" aria-label="Warmly lit restaurant table set with wine glasses"></div>
<div class="abs card-photo" role="img" aria-label="Hand holding a rewards benefits card"></div>
<div class="abs about-brand display">Kindly Yours<br>Rewards</div>

<h2 class="abs section-title about-title display">About Us</h2>
<div class="abs about-copy">
  <p>We provide marketing incentives in the form of gift certificates and vouchers that are redeemable for a variety of items such as: discount travel, smart device products, restaurant incentives , golf discounts and more to thousands of businesses around the world who use them to create exciting marketing promotions and giveaways, customer loyalty programs, promotional contests and use them as customer appreciation gifts.</p>
  <p>We are simply a 3rd party administrator that handles the redemption and fulfillment processing for a variety of incentive gifts and rewards. We have created the platform that facilitates the redemption and fulfillment process in a comprehensive, an easy to use online interface.</p>
</div>
<div class="abs read-more display">Read More</div>

<h2 id="testimonials" class="abs section-title testi-title display">Client Testimonails</h2>
<svg class="abs arrow" style="left:60px" width="28" height="40" viewBox="0 0 28 40"><path d="M24 3 6 20l18 17" fill="none" stroke="#111" stroke-width="3.5"/></svg>
<svg class="abs arrow" style="left:1114px" width="28" height="40" viewBox="0 0 28 40"><path d="M4 3l18 17L4 37" fill="none" stroke="#111" stroke-width="3.5"/></svg>

<article class="abs testimonial" style="left:111px">
  <blockquote>"Very good. Las Vegas was a dream trip. Would go again without a doubt. It's the best. The hotels, the streets, the Grand Canyon. Everything is very good!"</blockquote>
  <svg width="302" height="110" viewBox="0 0 302 110"><path d="M0 20c60-20 120 30 190 20S280 20 302 0v110H0z" fill="var(--cream)"/></svg>
  <div class="who"><strong>Lorena A.</strong><em>Orlando, FL</em></div>
</article>
<article class="abs testimonial" style="left:447px">
  <blockquote>“The trip to Vegas was the perfect getaway for my husband and I. The city that never stops. It has a little of everything from sight seeing to fun all-night options. We had a blast!!!”</blockquote>
  <svg width="302" height="110" viewBox="0 0 302 110"><path d="M0 20c60-20 120 30 190 20S280 20 302 0v110H0z" fill="var(--cream)"/></svg>
  <div class="who"><strong>Marisol P.</strong><em>Flagstaff, AZ</em></div>
</article>
<article class="abs testimonial" style="left:783px">
  <blockquote>“It was GREAT! I've always wanted to go to Vegas. Being able to stay right on the strip was great. I love that we were able to walk to a lot of the sites. The fountains at the Fontana Grand were AMAZING! I LOVED the atmosphere”</blockquote>
  <svg width="302" height="110" viewBox="0 0 302 110"><path d="M0 20c60-20 120 30 190 20S280 20 302 0v110H0z" fill="var(--cream)"/></svg>
  <div class="who"><strong>Hailey C.</strong><em>Bay Springs. MS</em></div>
</article>

<h2 class="abs section-title clients-title display">Our Clients</h2>
<div class="abs client" style="left:86px">HomeCrate</div>
<div class="abs client" style="left:347px">Harbor Realty</div>
<div class="abs client" style="left:609px">SkyBeam TV</div>
<div class="abs client" style="left:871px">Wellpath Plan</div>
<div class="abs dots"><i class="on"></i><i></i><i></i><i></i></div>

<footer class="abs site-footer display">© Copyright 2005-2025. All Rights Reserved.</footer>

</body>
</html>
```